Fire Hydrant Repair Parts Flyer

We need a flyer advertising both fire hydrant parts and the manufacturers that we are stocking. Our company is Coastal Flowline Supply and we are a parts distributor who sells directly to contractors. I have attached an example flyer that advertises some other parts we stock. We don't want it to look exactly like the old flyer, but we would like it to be structured similarly. I have also attached a background image for the flyer as well as some pictures of the parts we are stocking. I have also attached pictures of the manufacturer logos that we are stocking. We are trying to convey the parts that we are stocking which are: "Traffic Repair Kits", "Main Valve Repair Kits", "Extension Kits", "Replacement Caps & Gaskets", "Replacement Nozzles", Adjustable Hydrant Wrenches", "Hydrant Diffusers", & "Hydrant Oil". I have attached pictures of some of these items that we would like placed on the flyer. Let me know if you have any questions at all.

```html
<!DOCTYPE html>
<html lang="en">
<head>
<meta charset="utf-8">
<title>Fire Hydrant Repair Parts – Coastal Flowline Supply</title>
<link href="https://fonts.googleapis.com/css2?family=Montserrat:wght@400;500;600;700;800;900&display=swap" rel="stylesheet">
<style>
  :root{
    --navy:#1d2858;
    --pink:#e5195c;
    --white:#ffffff;
    --ink:#1f2233;
    --badge:#d9dce4;
    --stage:#eef0f4;
  }
  *{box-sizing:border-box;margin:0;padding:0}
  html,body{width:784px;height:1200px;overflow:hidden;background:var(--stage)}
  body{font-family:"Montserrat",sans-serif;color:var(--ink)}
  .flyer{position:relative;width:784px;height:1200px;background:var(--white);overflow:hidden}

  .brand-bar{position:absolute;top:0;left:0;width:100%;height:96px;display:flex;align-items:center;padding-left:56px;gap:12px}
  .brand-mark{width:26px;height:26px;background:var(--pink)}
  .brand-name{font-weight:700;font-size:22px;color:var(--navy);letter-spacing:.2px}

  .hero{position:absolute;top:96px;left:0;width:784px;height:500px}
  .hero-photo{position:absolute;inset:0;background:linear-gradient(180deg,#6e8a4f 0%,#8da66a 30%,#b0454a 52%,#c7d0d6 78%,#f1f3f5 100%)}
  .hero-shape{position:absolute;inset:0}
  .hero-copy{position:absolute;top:120px;left:56px;width:330px;color:var(--white)}
  .hero-kicker{font-weight:800;font-size:34px;line-height:1;letter-spacing:.5px}
  .hero-title{font-weight:900;font-size:78px;line-height:.95;color:var(--pink);letter-spacing:1px;margin-top:4px}
  .hero-sub{font-weight:800;font-size:22px;letter-spacing:.6px;margin-top:6px}
  .hero-intro{font-weight:500;font-size:13px;line-height:1.5;margin-top:22px;width:290px;opacity:.95}

  .stock-panel{position:absolute;top:560px;left:64px;width:656px;height:218px;background:var(--pink);border-radius:18px;padding:62px 40px 0 72px}
  .stock-label{position:absolute;top:-20px;left:50%;transform:translateX(-50%);background:var(--white);color:var(--navy);border-radius:30px;padding:11px 34px;font-size:19px;letter-spacing:.5px;white-space:nowrap;box-shadow:0 3px 10px rgba(0,0,0,.12)}
  .stock-label b{font-weight:800}
  .stock-label span{font-weight:500}
  .stock-list{display:grid;grid-template-columns:1fr 1fr;column-gap:40px;row-gap:9px;list-style:none}
  .stock-list li{position:relative;padding-left:20px;color:var(--white);font-weight:700;font-size:15px;line-height:1.2}
  .stock-list li::before{content:"";position:absolute;left:0;top:5px;width:9px;height:9px;border-radius:50%;background:var(--white)}

  .parts-row{position:absolute;top:812px;left:40px;width:704px;display:grid;grid-template-columns:repeat(7,1fr);gap:12px}
  .part{text-align:center}
  .part-photo{height:100px;border-radius:8px;background:linear-gradient(180deg,#eceef2,#c3c8d0)}
  .part-photo.red{background:linear-gradient(180deg,#f3e3e3,#cf3c3c)}
  .part-photo.gold{background:linear-gradient(180deg,#f4ecd8,#d6a43a)}
  .part-caption{font-size:10px;font-weight:600;color:var(--navy);margin-top:7px;line-height:1.25}

  .maker-row{position:absolute;top:968px;left:0;width:784px;display:flex;justify-content:center;gap:34px;align-items:center}
  .maker-badge{width:92px;height:36px;border-radius:6px;background:var(--badge)}
  .maker-badge.round{width:40px;height:40px;border-radius:50%}

  .footer{position:absolute;bottom:0;left:0;width:100%;height:150px;background:var(--navy);display:flex;align-items:center;justify-content:space-between;padding:0 44px;color:var(--white);font-size:14px;font-weight:600}
  .footer::before{content:"";position:absolute;top:-8px;left:0;width:100%;height:8px;background:var(--pink)}
  .contact{display:flex;align-items:center;gap:9px;white-space:nowrap}
  .contact svg{width:26px;height:26px;flex:none}
</style>
</head>
<body>
<main class="flyer">

  <header class="brand-bar">
    <span class="brand-mark"></span>
    <span class="brand-name">Coastal Flowline Supply</span>
  </header>

  <section class="hero">
    <div class="hero-photo" role="img" aria-label="Photo of a red fire hydrant on a lawn spraying a wide white burst of water"></div>
    <svg class="hero-shape" viewBox="0 0 784 500" preserveAspectRatio="none" aria-hidden="true">
      <polygon points="0,0 448,0 388,500 0,500" fill="#1d2858" opacity=".96"/>
      <polygon points="448,0 462,0 402,500 388,500" fill="#e5195c"/>
    </svg>
    <div class="hero-copy">
      <p class="hero-kicker">FIRE HYDRANT</p>
      <h1 class="hero-title">REPAIR</h1>
      <p class="hero-sub">PARTS AND ACCESSORIES</p>
      <p class="hero-intro">Coastal Flowline Supply and we are a parts distributor who sells directly to contractors.</p>
    </div>
  </section>

  <section class="stock-panel">
    <h2 class="stock-label"><b>PRODUCTS</b> <span>IN STOCK</span></h2>
    <ul class="stock-list">
      <li>Traffic Repair Kits</li>
      <li>Replacement Nozzles</li>
      <li>Main Valve Repair Kits</li>
      <li>Adjustable Hydrant Wrenches</li>
      <li>Extension Kits</li>
      <li>Hydrant Diffusers</li>
      <li>Replacement Caps &amp; Gaskets</li>
      <li>Hydrant Oil</li>
    </ul>
  </section>

  <section class="parts-row">
    <figure class="part"><div class="part-photo red" role="img" aria-label="Photo of a hydrant traffic repair kit"></div><figcaption class="part-caption">Traffic Repair Kit</figcaption></figure>
    <figure class="part"><div class="part-photo" role="img" aria-label="Photo of main valve repair kit parts"></div><figcaption class="part-caption">Main Valve Kit</figcaption></figure>
    <figure class="part"><div class="part-photo" role="img" aria-label="Photo of a hydrant extension kit"></div><figcaption class="part-caption">Extension Kit</figcaption></figure>
    <figure class="part"><div class="part-photo" role="img" aria-label="Photo of an adjustable hydrant wrench"></div><figcaption class="part-caption">Hydrant Wrench</figcaption></figure>
    <figure class="part"><div class="part-photo gold" role="img" aria-label="Photo of a hydrant diffuser"></div><figcaption class="part-caption">Hydrant Diffuser</figcaption></figure>
    <figure class="part"><div class="part-photo" role="img" aria-label="Photo of a bottle of hydrant oil"></div><figcaption class="part-caption">Hydrant Oil</figcaption></figure>
    <figure class="part"><div class="part-photo red" role="img" aria-label="Photo of replacement caps and gaskets"></div><figcaption class="part-caption">Caps &amp; Gaskets</figcaption></figure>
  </section>

  <section class="maker-row" aria-label="Manufacturers stocked">
    <span class="maker-badge round"></span>
    <span class="maker-badge"></span>
    <span class="maker-badge"></span>
    <span class="maker-badge"></span>
    <span class="maker-badge round"></span>
  </section>

  <footer class="footer">
    <span class="contact">
      <svg viewBox="0 0 24 24"><circle cx="12" cy="12" r="12" fill="#e5195c"/><path d="M8.6 6.5l2 2.1-1.1 1.6a7 7 0 0 0 4.3 4.3l1.6-1.1 2.1 2-1.2 1.6c-4.4.2-9-4.4-8.8-8.8z" fill="#fff"/></svg>
      (555) 014-2290
    </span>
    <span class="contact">
      <svg viewBox="0 0 24 24"><circle cx="12" cy="12" r="12" fill="#e5195c"/><rect x="6" y="8" width="12" height="8" rx="1" fill="#fff"/><path d="M6.5 8.5L12 12.5l5.5-4" stroke="#e5195c" stroke-width="1.2" fill="none"/></svg>
      sales@coastalflowline.com
    </span>
    <span class="contact">
      <svg viewBox="0 0 24 24"><circle cx="12" cy="12" r="12" fill="#e5195c"/><circle cx="12" cy="12" r="6" stroke="#fff" stroke-width="1.4" fill="none"/><path d="M6 12h12M12 6c-2.5 3-2.5 9 0 12M12 6c2.5 3 2.5 9 0 12" stroke="#fff" stroke-width="1.2" fill="none"/></svg>
      www.coastalflowline.com
    </span>
  </footer>

</main>
</body>
</html>
```